Business Card for Pottery and Jewellery Designer

A new business card design is needed to accompany a newly launching pottery and jewellery website. The company logo has been attached for use. The company is called Glazewick Studio. For a sense of the vibe please see the website (it is currently under construction but this way you'll get a feel for the style) www.GlazewickStudio.com

The website font is Pontano Sans for the body of the text with Overlock for headers.

The overall look should be clean and elegant. The back side can have just the logo. The front side should have a smaller logo and the following details displayed:

Glazewick Studio
Designer: Hollis Marrow
Phone: xxx.xxx.xxxx
Email: Designer@GlazewickStudio.com

The structure of displaying this is completely up to you. Different layouts and creative methods of displaying contact info are welcome as long as it stays clean/uncluttered.

No product photographs are to be included in the design as the catalogue changes quickly.

Colour preferences lean towards elegant and understated (charcoal grey, dark navy blue etc.)

Please let me know if you have any further questions or further details required.

Target Market(s)

Target market is 30+ year old women

Industry/Entity Type

Construction

Colors
ffffff
1b1b1b
474747
d9d9d9
fafafa
0355a3

Requirements
Must have
• The submissions so far have looked very typical and don't stand out right now. They're also all in navy with very little variation. I'm looking for something that stands out a it more while still being clean-looking.
Nice to have
• I've attached a few design samples and an idea for a backdrop. It would be great to see some designs in black, white, and grey with only a hint of color.
Should not have
• Product Images

```html
<!DOCTYPE html>
<html lang="en">
<head>
<meta charset="utf-8">
<title>Glazewick Studio — Business Card</title>
<link rel="stylesheet" href="https://fonts.googleapis.com/css2?family=Cinzel:wght@400&family=Overlock:wght@700&family=Lato:wght@400&display=swap">
<style>
  :root {
    --navy: #27265f;
    --ink-grey: #5a5a5a;
    --icon-grey: #8c8c8c;
    --rule-grey: #8a8a8a;
    --card-edge: #777777;
    --mist: #dcdcdc;
    --paper: #ffffff;
  }
  html, body {
    margin: 0;
    padding: 0;
    width: 892px;
    height: 1200px;
    overflow: hidden;
    background: var(--paper);
  }
  .sheet {
    position: relative;
    width: 892px;
    height: 1200px;
  }
  .card {
    position: absolute;
    box-sizing: border-box;
  }

  /* Front */
  .card--front {
    left: 29px; top: 53px;
    width: 836px; height: 474px;
    border: 1px solid var(--card-edge);
    background: var(--paper);
  }
  .brand-mark {
    position: absolute;
    border-radius: 50%;
    background: var(--mist);
  }
  .card--front .brand-mark {
    left: 126px; top: 56px;
    width: 92px; height: 92px;
  }
  .brand-name {
    position: absolute;
    margin: 0;
    font-family: "Cinzel", serif;
    font-weight: 400;
    color: var(--navy);
    text-align: center;
    line-height: 1;
  }
  .brand-name span { display: block; }
  .card--front .brand-name {
    left: 60px; top: 165px;
    width: 250px;
    font-size: 27px;
    letter-spacing: 4px;
  }
  .card--front .brand-name span + span {
    font-size: 22px;
    margin-top: 6px;
  }
  .accent-lines {
    position: absolute;
    left: 0; top: 0;
    width: 836px; height: 474px;
    pointer-events: none;
  }
  .social {
    position: absolute;
    left: 596px; top: 110px;
    display: flex;
    gap: 23px;
  }
  .social__dot {
    width: 39px; height: 39px;
    border-radius: 50%;
    background: var(--icon-grey);
  }
  .contact {
    position: absolute;
    left: 344px; top: 305px;
    font-family: "Lato", sans-serif;
  }
  .contact__role {
    margin: 0 0 0 66px;
    font-size: 14px;
    color: var(--ink-grey);
  }
  .contact__name {
    margin: 2px 0 0 66px;
    font-family: "Overlock", sans-serif;
    font-weight: 700;
    font-size: 35px;
    letter-spacing: 1px;
    color: var(--navy);
    line-height: 1.05;
  }
  .contact__row {
    display: flex;
    align-items: center;
    margin-top: 4px;
  }
  .contact__icon {
    width: 30px; height: 24px;
    margin: 0 30px 0 28px;
    fill: var(--ink-grey);
  }
  .contact__phone {
    font-size: 26px;
    color: var(--navy);
  }
  .contact__email {
    font-size: 22px;
    color: var(--ink-grey);
  }

  /* Back */
  .card--back {
    left: 29px; top: 709px;
    width: 837px; height: 476px;
    background: var(--navy);
  }
  .card--back .panel {
    position: absolute;
    left: 19px; top: 29px;
    width: 803px; height: 423px;
    background: var(--paper);
    clip-path: polygon(0 2%, 30% 0, 62% 1.5%, 100% 0, 99.4% 35%, 100% 70%, 99% 100%, 55% 98.5%, 20% 100%, 0.6% 99%, 0 60%, 1% 30%);
  }
  .card--back .brand-mark {
    left: 333px; top: 98px;
    width: 170px; height: 170px;
  }
  .card--back .brand-name {
    left: 0; top: 283px;
    width: 837px;
    font-size: 46px;
    letter-spacing: 7px;
  }
  .card--back .brand-name span + span {
    font-size: 36px;
    margin-top: 8px;
  }
</style>
</head>
<body>
<main class="sheet">

  <section class="card card--front" aria-label="Business card front">
    <div class="brand-mark" aria-hidden="true"></div>
    <h1 class="brand-name"><span>Glazewick</span><span>Studio</span></h1>

    <svg class="accent-lines" viewBox="0 0 836 474" aria-hidden="true">
      <line x1="309" y1="184" x2="404" y2="110" stroke="var(--rule-grey)" stroke-width="1"/>
      <line x1="119" y1="335" x2="215" y2="260" stroke="var(--rule-grey)" stroke-width="1"/>
    </svg>

    <div class="social" aria-label="Social links">
      <span class="social__dot"></span>
      <span class="social__dot"></span>
      <span class="social__dot"></span>
    </div>

    <div class="contact">
      <p class="contact__role">Designer</p>
      <p class="contact__name">HOLLIS MARROW</p>
      <div class="contact__row">
        <svg class="contact__icon" viewBox="0 0 30 24" aria-hidden="true">
          <path d="M3 11c5-8 19-8 24 0l-4 3-3-3v-3c-3-1-7-1-10 0v3l-3 3z" transform="rotate(-25 15 12)"/>
        </svg>
        <span class="contact__phone">000.000.0000</span>
      </div>
      <div class="contact__row">
        <svg class="contact__icon" viewBox="0 0 30 24" aria-hidden="true">
          <path d="M2 3h26v2L15 14 2 5z"/>
          <path d="M2 8l13 9 13-9v13H2z"/>
        </svg>
        <span class="contact__email">Designer@GlazewickStudio.com</span>
      </div>
    </div>
  </section>

  <section class="card card--back" aria-label="Business card back">
    <div class="panel">
    </div>
    <div class="brand-mark" aria-hidden="true"></div>
    <h2 class="brand-name"><span>Glazewick</span><span>Studio</span></h2>
  </section>

</main>
</body>
</html>
```